Business Card New Design for Corvella

We would like a new look on our business card, using the same style, the same colors blue, gray and white with similar font that is represented on the new Sell Sheet. We recently re-designed our Sell Sheets - I've attached a sell sheet file for your reference. I've also attached our current business card and our logo. Keep the same information listed on each side of the card.

Contact Information for Business Card

Use details given on example provided

Font styles to use
Other font styles liked:
• Myriad Regular and Bold

Colors

Designer to choose colors to be used in the design.

Requirements
Must have
• Current Information that was provided on the current business card. Colors Must use Blue, Gray and White, the same colors as the sell sheet example.

```html
<!DOCTYPE html>
<html lang="en">
<head>
<meta charset="utf-8">
<title>Corvella Business Card</title>
<link rel="stylesheet" href="https://fonts.googleapis.com/css2?family=Montserrat:wght@400;500;600;700&display=swap">
<style>
  :root {
    --brand-blue: #1241a0;
    --brand-blue-deep: #0d3585;
    --ink: #1c1c1c;
    --gray: #6b6b6b;
    --rule-gray: #8a8a8a;
    --paper: #ffffff;
    --paper-shade: #ececec;
    --backdrop: #2b2b2b;
  }
  * { box-sizing: border-box; margin: 0; padding: 0; }
  html, body { width: 1200px; height: 1200px; overflow: hidden; }
  body {
    background: var(--backdrop);
    font-family: "Montserrat", sans-serif;
    position: relative;
  }
  .card {
    position: absolute;
    left: 180px;
    width: 840px;
    height: 480px;
    overflow: hidden;
  }
  /* ---------- back ---------- */
  .card-back {
    top: 90px;
    background: linear-gradient(180deg, var(--brand-blue) 0%, var(--brand-blue-deep) 100%);
    color: var(--paper);
    text-align: center;
  }
  .card-back .wordmark {
    margin-top: 62px;
    font-size: 58px;
    font-weight: 700;
    letter-spacing: 10px;
    text-transform: uppercase;
    color: var(--paper);
  }
  .card-back .glow-rule {
    width: 560px;
    height: 2px;
    margin: 22px auto 26px;
    background: linear-gradient(90deg, rgba(255,255,255,0), rgba(255,255,255,0.75), rgba(255,255,255,0));
  }
  .service-list {
    list-style: none;
    font-variant: small-caps;
    font-size: 22px;
    font-weight: 500;
    line-height: 30px;
    letter-spacing: 0.6px;
  }
  /* ---------- front ---------- */
  .card-front {
    top: 630px;
    background: linear-gradient(135deg, var(--paper-shade) 0%, var(--paper) 55%);
  }
  .card-front .wordmark {
    position: absolute;
    top: 40px;
    left: 0;
    width: 100%;
    text-align: center;
    font-size: 50px;
    font-weight: 700;
    letter-spacing: 9px;
    text-transform: uppercase;
    color: var(--brand-blue);
  }
  .company-name {
    position: absolute;
    top: 122px;
    left: 0;
    width: 100%;
    text-align: center;
    font-variant: small-caps;
    font-size: 30px;
    font-weight: 700;
    letter-spacing: 0.5px;
    color: var(--brand-blue);
  }
  .person {
    position: absolute;
    top: 212px;
    right: 470px;
    text-align: right;
  }
  .person-name {
    font-size: 30px;
    font-weight: 600;
    color: var(--brand-blue);
  }
  .person-title {
    font-size: 26px;
    font-weight: 600;
    color: var(--ink);
    margin-top: 2px;
  }
  .divider {
    position: absolute;
    top: 182px;
    left: 408px;
    width: 1px;
    height: 190px;
    background: var(--rule-gray);
  }
  .contact-list {
    position: absolute;
    top: 186px;
    left: 440px;
    list-style: none;
    font-size: 19px;
    line-height: 30px;
    color: var(--ink);
  }
  .address-band {
    position: absolute;
    left: 0;
    bottom: 0;
    width: 100%;
    height: 82px;
    background: var(--brand-blue);
    color: var(--paper);
    display: flex;
    align-items: center;
    justify-content: center;
    gap: 12px;
    font-size: 26px;
    font-weight: 600;
  }
  .address-band svg { width: 22px; height: 30px; }
</style>
</head>
<body>

  <section class="card card-back">
    <div class="wordmark">Corvella</div>
    <div class="glow-rule"></div>
    <ul class="service-list">
      <li>Conveyors</li>
      <li>Target Sauce Applicators</li>
      <li>Target Topping Applicators</li>
      <li>Waterfall Topping Applicators</li>
      <li>Pepperoni / Meat Slicer / Applicators</li>
      <li>Portion Controlled Filler Pumps</li>
      <li>Dry Ingredient Applicators</li>
      <li>Check Weigh Conveyors</li>
      <li>Portion Compensators</li>
    </ul>
  </section>

  <section class="card card-front">
    <div class="wordmark">Corvella</div>
    <div class="company-name">Corvella Technical Services, Inc.</div>

    <div class="person">
      <div class="person-name">Daniel Reyes</div>
      <div class="person-title">CEO</div>
    </div>

    <div class="divider"></div>

    <ul class="contact-list">
      <li>Toll Free: (888) 555-0142 x226</li>
      <li>Phone: (815) 555-0142</li>
      <li>Direct: (815) 555-0187</li>
      <li>Cell: (815) 555-0123</li>
      <li>E-mail: dreyes@c-t-s.com</li>
      <li>Web: www.c-t-s.com</li>
    </ul>

    <div class="address-band">
      <svg viewBox="0 0 22 30" aria-hidden="true">
        <path d="M11 1C5.5 1 1.5 5 1.5 10.3 1.5 17 11 29 11 29s9.5-12 9.5-18.7C20.5 5 16.5 1 11 1z" fill="none" stroke="currentColor" stroke-width="2.4"/>
        <circle cx="11" cy="10.5" r="3.4" fill="currentColor"/>
      </svg>
      <span>4178 Harborview Road Millbrook, IL 60536</span>
    </div>
  </section>

</body>
</html>
```